Digital content business needs banner ads

We sell content - if you need an article to put on your website or in a newsletter, you can purchase a ready made article from us and edit it to your liking to use straight away. This could be any kind of article, but this banner ad will be aimed at real estate agents. You can see the website (and the style of articles) here https://www.thebluelanternpost.com.au
The banner is meant to solve the problem of the front desk admin or agent trying to think of something to write to put in their email newsletter. This will save them time as they can just select an article from our library and use it (for a fee of course!).
Needs to have the words:
--------------------------------------------------
Find the next article for your newsletter
---------------------------------------------------
Some imagery would be good rather than plain text.
With a call to action like click here button or similar
Required sizes (or provide a set of standard sized ads):
728 x 90
970 x 250
300x250
Real Estate Agents

```html
<!DOCTYPE html>
<html lang="en">
<head>
<meta charset="utf-8">
<title>The Blue Lantern Post – Banner Set</title>
<link rel="stylesheet" href="https://fonts.googleapis.com/css2?family=Montserrat:wght@500;700&display=swap">
<style>
  :root {
    --canvas: #d6d6d6;
    --panel: #454545;
    --accent: #1a7cc1;
    --white: #ffffff;
    --brand: #1b5f9e;
    --photo-light: #eeeae4;
    --photo-mid: #c9bcaa;
    --photo-warm: #b98a58;
    --photo-cool: #d9dde2;
  }
  * { box-sizing: border-box; margin: 0; padding: 0; }
  html, body { width: 1200px; height: 420px; overflow: hidden; }
  body {
    background: var(--canvas);
    font-family: "Montserrat", Arial, sans-serif;
    position: relative;
  }
  .banner {
    position: absolute;
    left: 18px;
    height: 108px;
    background: var(--panel);
    overflow: hidden;
  }
  .banner--leaderboard-large { top: 18px; width: 1164px; }
  .banner--leaderboard { top: 156px; width: 874px; }
  .banner--leaderboard-plain { top: 294px; width: 874px; }
  .banner__art { position: absolute; inset: 0; width: 100%; height: 100%; }
  .brand {
    position: absolute;
    left: 14px;
    top: 50%;
    transform: translateY(-50%);
    display: flex;
    align-items: center;
    gap: 7px;
    padding: 8px 10px;
    background: var(--white);
    border-radius: 6px;
  }
  .brand__mark { width: 12px; height: 12px; background: var(--accent); flex: none; }
  .brand__name {
    font-weight: 700;
    font-size: 13px;
    line-height: 1.1;
    color: var(--brand);
    width: 92px;
    text-transform: uppercase;
  }
  .headline {
    position: absolute;
    top: 50%;
    transform: translate(-50%, -50%);
    color: var(--white);
    font-weight: 500;
    text-align: center;
    line-height: 1.3;
    white-space: nowrap;
  }
  .headline strong { font-weight: 700; }
  .banner--leaderboard-large .headline { left: 738px; font-size: 26px; }
  .banner--leaderboard .headline,
  .banner--leaderboard-plain .headline { left: 522px; font-size: 23px; }
  .cta {
    position: absolute;
    display: flex;
    align-items: center;
    justify-content: center;
    height: 48px;
    background: var(--accent);
    border-right: 3px solid var(--white);
    color: var(--white);
    font-weight: 500;
    font-size: 18px;
    text-decoration: none;
  }
  .banner--leaderboard-large .cta { left: 988px; top: 34px; width: 161px; }
  .banner--leaderboard .cta { left: 720px; top: 32px; width: 145px; }
  .banner--leaderboard-plain .cta { left: 691px; top: 29px; width: 158px; }
</style>
</head>
<body>

<section class="banner banner--leaderboard-large" aria-label="970 by 250 style leaderboard banner">
  <svg class="banner__art" viewBox="0 0 1164 108" preserveAspectRatio="none">
    <defs>
      <linearGradient id="photo-desk-a" x1="0" y1="0" x2="1" y2="1">
        <stop offset="0" stop-color="var(--photo-light)"/>
        <stop offset="0.55" stop-color="var(--photo-mid)"/>
        <stop offset="1" stop-color="var(--photo-warm)"/>
      </linearGradient>
      <linearGradient id="photo-house-a" x1="0" y1="0" x2="1" y2="1">
        <stop offset="0" stop-color="var(--photo-cool)"/>
        <stop offset="1" stop-color="var(--photo-light)"/>
      </linearGradient>
    </defs>
    <polygon role="img" aria-label="Photo: magnifying glass over small wooden house models on a desk" points="0,0 552,0 510,108 0,108" fill="url(#photo-desk-a)"/>
    <polygon points="552,0 566,0 524,108 510,108" fill="var(--accent)"/>
    <polygon points="948,0 954,0 924,108 918,108" fill="var(--white)"/>
    <polygon role="img" aria-label="Photo: small model house on an agent's desk" points="954,0 1164,0 1164,108 924,108" fill="url(#photo-house-a)"/>
  </svg>
  <div class="brand"><span class="brand__mark"></span><span class="brand__name">The Blue Lantern Post</span></div>
  <p class="headline"><strong>Find</strong> the <strong>next article</strong><br>for <strong>your newsletter</strong></p>
  <a class="cta" href="https://www.thebluelanternpost.com.au">Click Here</a>
</section>

<section class="banner banner--leaderboard" aria-label="728 by 90 leaderboard banner">
  <svg class="banner__art" viewBox="0 0 874 108" preserveAspectRatio="none">
    <defs>
      <linearGradient id="photo-desk-b" x1="0" y1="0" x2="1" y2="1">
        <stop offset="0" stop-color="var(--photo-light)"/>
        <stop offset="0.55" stop-color="var(--photo-mid)"/>
        <stop offset="1" stop-color="var(--photo-warm)"/>
      </linearGradient>
      <linearGradient id="photo-house-b" x1="0" y1="0" x2="1" y2="1">
        <stop offset="0" stop-color="var(--photo-cool)"/>
        <stop offset="1" stop-color="var(--photo-light)"/>
      </linearGradient>
    </defs>
    <polygon role="img" aria-label="Photo: magnifying glass over small wooden house models on a desk" points="0,0 366,0 348,108 0,108" fill="url(#photo-desk-b)"/>
    <polygon points="366,0 378,0 360,108 348,108" fill="var(--accent)"/>
    <polygon points="690,0 696,0 674,108 668,108" fill="var(--white)"/>
    <polygon role="img" aria-label="Photo: small model house on an agent's desk" points="696,0 874,0 874,108 674,108" fill="url(#photo-house-b)"/>
  </svg>
  <div class="brand"><span class="brand__mark"></span><span class="brand__name">The Blue Lantern Post</span></div>
  <p class="headline"><strong>Find</strong> the <strong>next article</strong><br>for <strong>your newsletter</strong></p>
  <a class="cta" href="https://www.thebluelanternpost.com.au">Click Here</a>
</section>

<section class="banner banner--leaderboard-plain" aria-label="728 by 90 leaderboard banner, single image">
  <svg class="banner__art" viewBox="0 0 874 108" preserveAspectRatio="none">
    <defs>
      <linearGradient id="photo-desk-c" x1="0" y1="0" x2="1" y2="1">
        <stop offset="0" stop-color="var(--photo-light)"/>
        <stop offset="0.55" stop-color="var(--photo-mid)"/>
        <stop offset="1" stop-color="var(--photo-warm)"/>
      </linearGradient>
    </defs>
    <polygon role="img" aria-label="Photo: magnifying glass over small wooden house models on a desk" points="0,0 342,0 336,108 0,108" fill="url(#photo-desk-c)"/>
    <polygon points="342,0 353,0 347,108 336,108" fill="var(--accent)"/>
  </svg>
  <div class="brand"><span class="brand__mark"></span><span class="brand__name">The Blue Lantern Post</span></div>
  <p class="headline"><strong>Find</strong> the <strong>next article</strong><br>for <strong>your newsletter</strong></p>
  <a class="cta" href="https://www.thebluelanternpost.com.au">Click Here</a>
</section>

</body>
</html>
```